Massage Clinic needs a Flyer for Advertising

Our massage clinic, 'Keel Line Massage Therapy', has recently opened in Osborne Park, Western Australia. We are specialists in deep tissue and sports massage. We also offer relaxation, trigger point therapy, stretching techniques, and postural and functional movement analysis. We're based within the same building complex as a personal training and Ironvane box. There are also a number of local gyms in the area. Our target clients are both the local athletes, but also local business (Osborne Park is a business district in Perth).

We need double-sided DL size flyer. We would like the design to incorporate the colouring of the logo (green, purple, grey), but happy for it to use anything that enhances this also. Logo has been attached (.png and .ai format). There is also a selection of photos available to use if required, other stylised images would also be accepted. We'd like the flyer to include business details, services, and price list (price list is optional). We can provide further descriptions of key therapies on offer if required for inclusion.

Target Market(s)

Local athletes (gym, Ironvane, sport), and local business employees.

Industry/Entity Type

Massage Therapy

Font styles to use
Sans Serif

Requirements
Must have
• List of Services to be included:
• Relaxation Massage
• Deep Tissue Massage
• Sports Massage
• Neuromuscular (Trigger Point) Therapy
• Postural Analysis
• Musculoskeletal and Functional Movement Screening
• Therapeutic Stretching (including Proprioceptive Neuromuscular Facilitation and Muscle Energy Technique)
• All sessions are customised to suit the needs of the client, and may incorporate a variety of the above techniques.
• Business location and Contact details:
• 4/18 Tamsin Road, Osborne Park WA 6017
• Phone: 0417 362 804
• Email: info@keelline.net.au
Nice to have
• Symbols for showing the company has Facebook and Instagram accounts.
• The business is also a member of GPRV - logo attached below, please include.
• Price details are shown in one of the attached images, and copied below:
• Individual -
• 30 minutes $45
• 60 minutes $85
• Packages -
• 4 x 30 minutes $165
• 4 x 60 minutes $305
• (Packages valid for two months; pre-payment required).
Should not have
• Please don't use any imagery/design that looks suited to a day-spa environment. My massage clinic is located within a gym environment.
• If you use stock photo's, please select one where the therapists hands are female (both are stuff are currently female therapists).

```html
<!DOCTYPE html>
<html lang="en">
<head>
<meta charset="utf-8">
<title>Keel Line Massage Therapy – Flyer</title>
<link rel="stylesheet" href="https://fonts.googleapis.com/css2?family=Roboto:wght@400;500;700&family=Roboto+Condensed:wght@400;700&display=swap">
<style>
  :root{
    --purple:#7b2f98;
    --purple-deep:#5e1f7a;
    --purple-light:#9c4fb8;
    --green:#8cc63f;
    --green-dark:#6fa82a;
    --white:#ffffff;
    --ink:#3d3d3d;
    --grey:#6b6b6b;
  }
  *{box-sizing:border-box;margin:0;padding:0}
  html,body{width:688px;height:1200px;overflow:hidden;background:#e9e9e9}
  .flyer{
    position:relative;width:688px;height:1200px;overflow:hidden;
    background:linear-gradient(180deg,var(--purple-light) 0%,var(--purple) 55%,var(--purple-deep) 100%);
    font-family:"Roboto",Arial,sans-serif;color:var(--white);
  }
  .flyer__shapes{position:absolute;left:0;top:0;width:688px;height:700px}
  .brand{
    position:absolute;top:48px;left:0;width:100%;
    display:flex;align-items:center;justify-content:center;gap:16px;
  }
  .brand__dot{width:34px;height:34px;border-radius:50%;background:var(--green)}
  .brand__name{
    font-family:"Roboto",Arial,sans-serif;font-weight:500;font-size:34px;
    color:var(--purple);letter-spacing:.3px;
  }
  .headline{
    position:absolute;top:676px;left:0;width:100%;text-align:center;
    font-family:"Roboto Condensed","Arial Narrow",sans-serif;
    font-size:74px;font-weight:400;color:var(--green);letter-spacing:1px;line-height:1;
  }
  .subline{
    position:absolute;top:758px;left:0;width:100%;text-align:center;
    font-family:"Roboto Condensed","Arial Narrow",sans-serif;
    font-size:35px;color:var(--white);letter-spacing:.5px;line-height:1;
  }
  .services__label{
    position:absolute;top:838px;left:30px;
    background:linear-gradient(90deg,var(--green) 0%,var(--green) 65%,rgba(140,198,63,0) 100%);
    padding:6px 90px 6px 16px;border-radius:16px 0 0 16px;
    font-family:"Roboto Condensed","Arial Narrow",sans-serif;font-weight:700;
    font-size:24px;letter-spacing:1px;color:var(--white);
  }
  .services__list{
    position:absolute;top:884px;left:40px;width:620px;
    display:grid;grid-template-columns:250px 1fr;column-gap:20px;
  }
  .services__list ul{list-style:none}
  .services__list li{
    position:relative;padding-left:22px;font-size:19px;line-height:26px;color:var(--white);
  }
  .services__list li::before{
    content:"";position:absolute;left:2px;top:9px;width:9px;height:9px;
    border-radius:50%;background:var(--green);
  }
  .footer{position:absolute;left:0;bottom:0;width:688px;height:150px}
  .footer svg{position:absolute;left:0;top:0}
  .contact{
    position:absolute;left:0;bottom:32px;width:100%;
    display:flex;justify-content:center;gap:56px;align-items:center;
    font-size:26px;color:var(--ink);
  }
  .contact__item{display:flex;align-items:center;gap:12px}
</style>
</head>
<body>
<main class="flyer">
  <svg class="flyer__shapes" viewBox="0 0 688 700" width="688" height="700" aria-hidden="false">
    <defs>
      <linearGradient id="photoLeft" x1="0" y1="0" x2="1" y2="1">
        <stop offset="0" stop-color="#c9d1d6"/>
        <stop offset=".55" stop-color="#e3c2a6"/>
        <stop offset="1" stop-color="#3f6fa2"/>
      </linearGradient>
      <linearGradient id="photoRight" x1="0" y1="0" x2="1" y2="1">
        <stop offset="0" stop-color="#e9e4de"/>
        <stop offset=".5" stop-color="#efcfb8"/>
        <stop offset="1" stop-color="#cfa58a"/>
      </linearGradient>
    </defs>
    <!-- white header area -->
    <rect x="0" y="0" width="688" height="620" fill="#ffffff"/>
    <!-- top purple swoosh -->
    <path d="M0,175 C160,215 280,240 344,330 C408,240 528,215 688,175 L688,205 C540,235 420,270 344,380 C268,270 148,235 0,205 Z" fill="var(--purple)"/>
    <!-- central purple lens -->
    <path d="M344,330 C300,420 300,540 344,640 C388,540 388,420 344,330 Z" fill="var(--purple)"/>
    <!-- left photo -->
    <path role="img" aria-label="Photo of a therapist's hands massaging a client's shoulder with a towel on a massage table" d="M0,215 C150,245 270,290 330,390 C290,470 290,560 330,640 L0,640 Z" fill="url(#photoLeft)"/>
    <!-- right photo -->
    <path role="img" aria-label="Photo of a relaxed client lying face up receiving a neck massage" d="M688,215 C538,245 418,290 358,390 C398,470 398,560 358,640 L688,640 Z" fill="url(#photoRight)"/>
    <!-- green arcs -->
    <path d="M0,160 C170,195 290,225 344,300 C398,225 518,195 688,160" fill="none" stroke="var(--green)" stroke-width="8"/>
    <!-- lower purple wave into body -->
    <path d="M0,600 C200,560 488,560 688,600 L688,700 L0,700 Z" fill="var(--purple-light)"/>
    <path d="M0,590 C200,548 488,548 688,590" fill="none" stroke="var(--green)" stroke-width="7"/>
  </svg>

  <header class="brand">
    <span class="brand__dot"></span>
    <span class="brand__name">Keel Line Massage Therapy</span>
  </header>

  <h1 class="headline">FEEL RELAXED</h1>
  <p class="subline">WITH OUR HEAVENLY THERAPY</p>

  <section class="services">
    <h2 class="services__label">SERVICES</h2>
    <div class="services__list">
      <ul>
        <li>Relaxation Massage</li>
        <li>Deep Tissue Massage</li>
        <li>Sports Massage</li>
        <li>Neuromuscular</li>
        <li>Trigger Point Therapy</li>
        <li>Postural Analysis</li>
      </ul>
      <ul>
        <li>Musculoskeletal and Functional<br>movement screening</li>
        <li>Therapeutic Stretching<br>including Proprioceptive</li>
        <li>Neuromuscular facilitation<br>and muscle energy technique</li>
      </ul>
    </div>
  </section>

  <footer class="footer">
    <svg viewBox="0 0 688 150" width="688" height="150" aria-hidden="true">
      <path d="M0,40 C220,5 468,5 688,40 L688,150 L0,150 Z" fill="var(--green)"/>
      <path d="M0,52 C220,18 468,18 688,52 L688,150 L0,150 Z" fill="#ffffff"/>
    </svg>
    <div class="contact">
      <span class="contact__item">
        <svg width="34" height="34" viewBox="0 0 24 24" aria-hidden="true">
          <circle cx="12" cy="12" r="12" fill="var(--green)"/>
          <path d="M8.6 6.5l1.8 2.4-1 1.3c.7 1.6 1.8 2.7 3.4 3.4l1.3-1 2.4 1.8-.9 1.9c-4.3-.2-8.3-4.2-8.5-8.5z" fill="#fff"/>
        </svg>
        0417 362 804
      </span>
      <span class="contact__item">
        <svg width="34" height="26" viewBox="0 0 34 26" aria-hidden="true">
          <rect x="1" y="1" width="32" height="24" rx="2" fill="var(--green)"/>
          <path d="M3 4l14 11 14-11" fill="none" stroke="#fff" stroke-width="2.2"/>
        </svg>
        info@keelline.net.au
      </span>
    </div>
  </footer>
</main>
</body>
</html>
```